Tobias Wrenfield Business Card

In addition to my name design (file uploaded), black print on white card stock, e-mail address should be presented as a typical e-mail address, i.e., underlined and in blue ink, the card should include the following information:
Professor of Aviation Technology
Accident Litigation Expert Witness
Master Certificated Flight Instructor

twrenfield@qorvanet.net
Anchorage, Alaska
(907) 518-2736

Industry/Entity Type

Business

```html
<!DOCTYPE html>
<html lang="en">
<head>
<meta charset="utf-8">
<title>Tobias Wrenfield Business Card</title>
<link href="https://fonts.googleapis.com/css2?family=Oswald:wght@500&family=Arimo:wght@400&display=swap" rel="stylesheet">
<style>
  :root {
    --backdrop: #cdcccd;
    --card: #ffffff;
    --ink: #0d0d0d;
    --link: #2b2ba0;
    --graphic: #d9d9d9;
  }
  * { margin: 0; padding: 0; box-sizing: border-box; }
  html, body {
    width: 1200px;
    height: 1000px;
    overflow: hidden;
    background: var(--backdrop);
  }
  .card {
    position: absolute;
    left: 69px;
    top: 205px;
    width: 1063px;
    height: 591px;
    background: var(--card);
    overflow: hidden;
  }
  .aircraft-graphic {
    position: absolute;
    left: 30px;
    top: 0;
    width: 540px;
    height: 591px;
  }
  .details {
    position: absolute;
    right: 64px;
    text-align: right;
    font-family: "Arimo", Arial, sans-serif;
    color: var(--ink);
  }
  .name {
    position: absolute;
    right: 62px;
    top: 68px;
    font-family: "Oswald", "Arial Narrow", sans-serif;
    font-weight: 500;
    font-size: 76px;
    line-height: 1;
    letter-spacing: 1px;
    text-transform: uppercase;
    color: var(--ink);
  }
  .credentials {
    top: 170px;
    font-size: 23.5px;
    line-height: 32px;
  }
  .contact {
    top: 426px;
    font-size: 23.5px;
    line-height: 34.5px;
  }
  .contact a {
    color: var(--link);
    text-decoration: underline;
    text-underline-offset: 4px;
  }
</style>
</head>
<body>
  <div class="card">
    <svg class="aircraft-graphic" viewBox="0 0 540 591" role="img" aria-label="Large pale grey silhouette of a jet airliner climbing diagonally across the card">
      <defs>
        <radialGradient id="aircraft-tone" cx="50%" cy="50%" r="55%">
          <stop offset="0%" stop-color="#d9d9d9"/>
          <stop offset="100%" stop-color="#ffffff"/>
        </radialGradient>
      </defs>
      <rect width="540" height="591" fill="url(#aircraft-tone)"/>
    </svg>

    <div class="name">Tobias Wrenfield</div>

    <div class="details credentials">
      <p>Professor of Aviation Technology</p>
      <p>Accident Litigation Expert Witness</p>
      <p>Master Certificated Flight Instructor</p>
    </div>

    <div class="details contact">
      <p><a href="mailto:twrenfield@qorvanet.net">twrenfield@qorvanet.net</a></p>
      <p>Anchorage, Alaska</p>
      <p>(907) 518-2736</p>
    </div>
  </div>
</body>
</html>
```